Whitepaper on Cyber Security for Community Banks & Credit Unions

I need to turn a basic whitepaper into a nice eBook we can use with a landing page on our website. We have several eBooks we publish so this is a test to see if we can being to use PixelMarsh to help with those projects. We are not done with final editing of the words so whatever is produced need to be editable on our side--however basic framework of the doc is complete (words might change in the paragraphs)

Target Market(s)

Bank and Credit Union Executive Managment

Industry/Entity Type

Security

Font styles to use
Serif
Sans Serif

Requirements
Must have
• works with our website design https://grelvanstone.com

```html
<!DOCTYPE html>
<html lang="en">
<head>
<meta charset="utf-8">
<title>Preparing for a Data Breach – Page 4</title>
<link href="https://fonts.googleapis.com/css2?family=Source+Sans+3:ital,wght@0,400;0,600;0,700;1,400&display=swap" rel="stylesheet">
<style>
  :root {
    --ink: #1a1a1a;
    --muted: #8a8a8a;
    --brand-dark: #1b2a3a;
    --brand-blue: #2a8fe0;
    --paper: #ffffff;
  }
  * { box-sizing: border-box; margin: 0; padding: 0; }
  html, body { width: 848px; height: 1200px; overflow: hidden; background: var(--paper); }
  body { font-family: "Source Sans 3", Arial, sans-serif; color: var(--ink); }
  .page { position: relative; width: 848px; height: 1200px; padding: 0 38px; }
  .running-head { position: absolute; top: 48px; left: 38px; font-size: 13.5px; color: var(--muted); }
  .brand { position: absolute; top: 52px; right: 44px; display: flex; align-items: center; gap: 10px; }
  .brand-mark { width: 30px; height: 30px; background: var(--brand-dark); }
  .brand-name { font-size: 30px; font-weight: 700; color: var(--brand-dark); letter-spacing: -0.3px; }
  .content { position: absolute; top: 108px; left: 38px; right: 36px; font-size: 13.6px; line-height: 17.4px; }
  h2 { font-size: 27px; font-weight: 700; line-height: 34px; }
  p { text-align: justify; }
  .bullets { list-style: none; margin: 6px 0 0 0; }
  .bullets li { position: relative; padding-left: 16px; margin-bottom: 4px; text-align: justify; }
  .bullets li::before { content: "•"; position: absolute; left: 4px; }
  .section-gap { margin-top: 36px; }
  .indent { padding-left: 16px; margin-top: 16px; }
  .indent + .indent { margin-top: 5px; }
  .numbered { margin-top: 4px; padding-left: 2px; }
  .checklist { list-style: none; margin: 26px 0 0 16px; }
  .checklist li { position: relative; padding-left: 16px; margin-bottom: 5.6px; text-align: justify; }
  .checklist li::before { content: "o"; position: absolute; left: 0; }
  .page-number { position: absolute; bottom: 28px; left: 0; right: 0; text-align: center; font-style: italic; font-size: 15px; color: var(--muted); }
</style>
</head>
<body>
<div class="page">
  <div class="running-head">Preparing for a Data Breach</div>
  <div class="brand" aria-label="Grelvanstone">
    <span class="brand-mark"></span>
    <span class="brand-name">Grelvanstone</span>
  </div>

  <main class="content">
    <h2>4.&nbsp; Helpful Organizations</h2>
    <p>There are also several organizations that provide a helping hand to both community banks and credit unions. This is not an exhaustive list by any means:</p>
    <ul class="bullets">
      <li>BANQLINK - The professional network for bank and credit union professionals, empowering them to collaborate, share information and lead the evolution of community banking.</li>
      <li>National Alliance of Member Credit Unions (NAMCU) - a direct membership association for federally insured credit unions committed to representing, assisting, educating and informing their member credit unions to help them grow, and help grow the credit union industry.</li>
      <li>Financial Sector - Threat Exchange Council (FS-TEC) – An industry forum for collaboration on critical security threats facing the global financial services sector.</li>
    </ul>

    <h2 class="section-gap">5.&nbsp; Regulatory Compliance &amp; Cyber Security</h2>
    <p>The Policy that primarily drives all cyber security with financial institutions at the Federal level is the Gramm-Leach-Bliley Safeguards rule. These laws impact both community banks and credit unions.</p>

    <ul class="bullets" style="margin-top:24px">
      <li>The Gramm–Leach–Bliley Act– (for details 6801–6809) GLBA requires financial institutions (companies that offer consumers financial products or services like loans, financial or investment advice, or insurance) to explain their information-sharing practices to their customers and to safeguard sensitive data. The Act contains three elements (Privacy Rule, Safeguards Rule and Pretexting Protection) regarding the privacy of information, of which businesses, primarily "financial institutions," need to be aware – for this paper we will cover the GLBA Safeguards Rule (More from the FTC).</li>
    </ul>
    <p class="indent" style="margin-top:4px">The Safeguards Rule requires an institution to develop, implement, and maintain a comprehensive information security program that is written, contains administrative, technical and physical safeguards, is “appropriate” to the institution’s size and complexity, as well as the nature and scope of its activities, and is appropriate to the sensitivity of the customer information at issue.</p>
    <p class="indent">The FTC requires (more here) companies to conduct a thorough risk assessment and address such risks to customer information in all areas of their operation, including administrative, technical, and physical safeguards. As part of the risk assessment, the Safeguards Rule requires an institution to:</p>
    <ul class="bullets">
      <li>Designate someone to coordinate the information security program;</li>
      <li>Perform a thorough risk assessment and identify reasonably foreseeable internal and external risks to the security, confidentiality, and integrity of customer information that could result in unauthorized disclosure, misuse, alteration, destruction or other compromise of such information, and assess the sufficiency of any safeguards in place to control these risks.</li>
    </ul>
    <p class="numbered">1.&nbsp; Employee Training and Management. A costs of compliance is related to employee training and management. A financial institution’s risk assessment should:</p>

    <ul class="checklist">
      <li>Check employee references and perform background checks;</li>
      <li>Require employees to sign a confidentiality agreement;</li>
      <li>Limit employee access to sensitive customer information;</li>
      <li>Use password-activated screen savers to lock employee computers;</li>
      <li>Encrypt customer files on laptops and other computers in case of theft;</li>
      <li>Impose disciplinary measures for security policy violations;</li>
      <li>Prevent terminated employees from accessing customer information by immediately deactivating their passwords and user names. The FTC noted in one of its publications that “the success of your information security plan depends largely upon the employees who implement it.”</li>
    </ul>
  </main>

  <div class="page-number">Page #4</div>
</div>
</body>
</html>
```